Brinewardsea.com Website design needed!!

We are looking for a website layout to match the attached logo. We specialize in Dive Charters and currently are located in the Virgin Islands off of St. Thomas. Please create a design that is compatible with Bootstrap and have the grid in mind. WE are looking for creative and extremely professional layout design.

Target Market(s)

Scuba Diving, Divers looking for a diving charter in the Virgin Islands.

Number of Pages Required

3 page

Font styles to use
Serif

Requirements
Must have
• Must be Bootstrap friendly.
• Must work with the logo we provided. Colors etc.

```html
<!DOCTYPE html>
<html lang="en">
<head>
<meta charset="utf-8">
<title>Brinewardsea.com – Dive Charters</title>
<link rel="stylesheet" href="https://fonts.googleapis.com/css2?family=Carlito:wght@400;700&family=Questrial&display=swap">
<style>
:root{
  --red:#ef1c25;
  --blue:#399ed7;
  --footer-blue:#44a7dc;
  --field-blue:#a6d5ee;
  --dark:#222222;
  --text:#666666;
  --heading:#222222;
  --white:#ffffff;
  --panel:#eeeeee;
  --line:#cccccc;
}
*{box-sizing:border-box;margin:0;padding:0}
html,body{width:1069px;height:1200px;overflow:hidden}
body{position:relative;font-family:"Carlito",Arial,sans-serif;color:var(--text);background:var(--white)}
.abs{position:absolute}

/* header */
.site-header{left:0;top:0;width:1069px;height:85px;background:var(--white)}
.brand{left:58px;top:26px;display:flex;align-items:center;gap:8px}
.brand-dot{width:30px;height:30px;border-radius:50%;background:var(--blue)}
.brand-name{font-family:"Carlito",sans-serif;font-weight:700;font-size:24px;color:var(--red)}
.contact-item{top:30px;text-align:right}
.contact-label{font-size:12px;color:var(--red);line-height:14px}
.contact-value{color:#666;line-height:18px}
.icon-box{top:31px;width:31px;height:28px;border:1px solid var(--red);display:flex;align-items:center;justify-content:center}

/* nav */
.main-nav{left:0;top:85px;width:1069px;height:59px;background:var(--blue)}
.nav-item{top:0;height:59px;line-height:59px;font-size:11.5px;color:var(--white);text-transform:uppercase}
.nav-item.active{left:42px;width:104px;background:var(--red);text-align:center}
.nav-cta{left:791px;top:0;width:235px;height:59px;background:var(--red);color:var(--white);text-align:center;padding-top:11px;font-size:14px;line-height:19px}
.nav-cta strong{font-size:17px;font-weight:400;display:block}

/* hero */
.hero{left:0;top:144px;width:1069px;height:455px;background:radial-gradient(ellipse at 50% 60%,#274a48 0%,#17312f 55%,#0e1f1d 100%)}
.hero-title{left:0;top:278px;width:1069px;text-align:center;font-family:"Questrial",sans-serif;font-size:41px;color:var(--white);letter-spacing:.5px}
.hero-text{left:160px;top:341px;width:749px;text-align:center;font-size:11px;line-height:20px;color:var(--white)}
.btn{background:var(--red);color:var(--white);text-transform:uppercase;display:flex;align-items:center;justify-content:center;font-size:11px}
.hero-btn{left:478px;top:429px;width:114px;height:36px;border:1px solid var(--white)}
.dot{top:510px;width:11px;height:11px;border-radius:50%;border:1.5px solid var(--white)}
.dot.on{background:var(--red)}

/* search panel */
.search-panel{left:42px;top:619px;width:237px;height:279px;background:linear-gradient(#f4f4f4,#e6e6e6);border:1px solid #d8d8d8}
.search-head{left:0;top:0;width:235px;height:37px;background:var(--red);color:var(--white);font-weight:700;font-size:17px;text-align:center;line-height:37px}
.field{left:19px;width:194px;height:28px;background:var(--white);border:1px solid #cfcfcf;font-size:10px;color:#999;padding:7px 10px}
.find-btn{left:20px;top:128px;width:194px;height:27px;font-size:11px}
.rule{top:174px;height:1px;width:81px;background:#aaa}
.or{left:0;top:166px;width:235px;text-align:center;font-size:13px;color:#666}
.connect{left:0;top:193px;width:235px;text-align:center;font-size:14px;color:#666}
.social-circle{top:214px;width:42px;height:42px;border-radius:50%}

/* welcome */
.welcome-title{left:319px;top:621px;font-family:"Questrial",sans-serif;font-size:28px;color:var(--heading)}
.welcome-title span{color:var(--red)}
.welcome-text{left:319px;top:668px;width:701px;font-size:11px;line-height:21.9px;color:#777;text-align:justify}
.welcome-btn{left:319px;top:851px;width:102px;height:29px}

/* footer */
.site-footer{left:0;top:939px;width:1069px;height:192px;background:var(--footer-blue)}
.footer-head{top:28px;font-size:16px;font-weight:700;color:var(--white);text-transform:uppercase;letter-spacing:.3px}
.footer-links{left:45px;top:60px;list-style:none}
.footer-links li{font-size:11px;color:var(--white);line-height:25.3px;display:flex;align-items:center;gap:7px}
.footer-links svg{flex:none}
.ffield{width:140px;height:36px;background:var(--field-blue);font-size:10.5px;font-style:italic;color:#6f8fa3;padding:11px 11px}
.submit{left:231px;top:143px;width:117px;height:34px;background:#333;color:var(--white);font-size:13px;display:flex;align-items:center;justify-content:center}
.q-list{left:586px;top:60px;font-size:11px;color:var(--white);line-height:25.3px}
.follow{top:71px;width:31px;height:31px;border-radius:50%;background:var(--white)}
.copyright{left:0;top:1131px;width:1069px;height:69px;background:var(--dark);color:var(--white);font-size:11px;text-align:center;line-height:66px}
</style>
</head>
<body>

<header class="site-header abs">
  <div class="brand abs">
    <span class="brand-dot"></span>
    <span class="brand-name">Brinewardsea.com</span>
  </div>
  <div class="contact-item abs" style="left:640px;width:166px">
    <div class="contact-label">Email id :</div>
    <div class="contact-value" style="font-size:12px">info@companyname.com</div>
  </div>
  <div class="icon-box abs" style="left:816px">
    <svg width="15" height="11" viewBox="0 0 15 11"><rect x="0.7" y="0.7" width="13.6" height="9.6" fill="none" stroke="#ef1c25" stroke-width="1.3"/><path d="M1 1 L7.5 6 L14 1" fill="none" stroke="#ef1c25" stroke-width="1.3"/></svg>
  </div>
  <div class="contact-item abs" style="left:860px;width:128px">
    <div class="contact-label" style="margin-top:-3px">Call Us</div>
    <div class="contact-value" style="font-size:16px;line-height:20px">123-456-7890</div>
  </div>
  <div class="icon-box abs" style="left:995px">
    <svg width="12" height="13" viewBox="0 0 24 24"><path d="M6.6 10.8c1.4 2.8 3.8 5.1 6.6 6.6l2.2-2.2c.3-.3.7-.4 1-.2 1.1.4 2.3.6 3.6.6.6 0 1 .4 1 1V20c0 .6-.4 1-1 1C10.6 21 3 13.4 3 4c0-.6.4-1 1-1h3.5c.6 0 1 .4 1 1 0 1.3.2 2.5.6 3.6.1.3 0 .7-.2 1z" fill="#ef1c25"/></svg>
  </div>
</header>

<nav class="main-nav abs">
  <div class="nav-item active abs">Brinewardsea</div>
  <div class="nav-item abs" style="left:186px">About Us</div>
  <div class="nav-item abs" style="left:295px">Contact</div>
  <div class="nav-item abs" style="left:397px">Learn More</div>
  <div class="nav-item abs" style="left:520px">Schedule</div>
  <div class="nav-cta abs">Search for Your Dream Charter<strong>TODAY!</strong></div>
</nav>

<section class="hero abs" role="img" aria-label="Underwater photograph of a scuba diver swimming above a reef"></section>
<h1 class="hero-title abs" style="font-weight:400">BRINEWARDSEA CHARTERS AND SCUBA</h1>
<p class="hero-text abs">Lorem ipsum dolor sit amet, consectetur adipiscing elit. Fusce semper vitae leo sit amet vehicula. Sed viverra, justo ac consectetur hendrerit, lacus elit tempor urna, gravida mattis lacus ex sed sem. Nam consectetur, arcu in iaculis dapibus, urna felis congue elit, in consectetur nisi massa sed metus. Nullam a tortor ut mauris auctor interdum id vel neque.</p>
<div class="btn hero-btn abs">Read More</div>
<span class="dot abs" style="left:510px"></span>
<span class="dot on abs" style="left:529px"></span>
<span class="dot abs" style="left:548px"></span>

<aside class="search-panel abs">
  <div class="search-head abs">Search for Your Dream</div>
  <div class="field abs" style="top:51px">Name</div>
  <div class="field abs" style="top:88px">Email id</div>
  <div class="btn find-btn abs">Find Charters</div>
  <span class="rule abs" style="left:20px"></span>
  <span class="rule abs" style="left:137px"></span>
  <div class="or abs">or</div>
  <div class="connect abs">Connect with</div>
  <span class="social-circle abs" style="left:74px;background:#3b5998" role="img" aria-label="Social network link"></span>
  <span class="social-circle abs" style="left:126px;background:#dd4b39" role="img" aria-label="Social network link"></span>
</aside>

<h2 class="welcome-title abs" style="font-weight:400">Welcome to <span>Brinewardsea</span></h2>
<p class="welcome-text abs">Lorem ipsum dolor sit amet, consectetur adipiscing elit. Fusce semper vitae leo sit amet vehicula. Sed viverra, justo ac consectetur hendrerit, lacus elit tempor urna, gravida mattis lacus ex sed sem. Nam consectetur, arcu in iaculis dapibus, urna felis congue elit, in consectetur nisi massa sed metus. Nullam a tortor ut mauris auctor interdum id vel neque. In commodo diam at faucibus dictum. Nulla condimentum elit a odio consectetur, vel eleifend libero sagittis. Praesent sed erat a ante laoreet dapibus et ultrices sem. Vivamus elit lectus, ullamcorper et vestibulum eget, venenatis eu nunc. In eu elit vestibulum, hendrerit velit sed, dignissim arcu. Vivamus sodales vestibulum nulla, ut posuere lectus faucibus tempor. Nullam at rhoncus velit. Duis massa ipsum, hendrerit et faucibus in, facilisis sed lorem. Vestibulum ac ligula vestibulum, rutrum ex vehicula, tempus nisl. Integer mi tortor, maximus quis fringilla a, dictum non ipsum. Maecenas venenatis pellentesque neque at facilisis. Etiam at nulla in neque molestie vestibulum.</p>
<div class="btn welcome-btn abs">Read More</div>

<footer class="site-footer abs">
  <div class="footer-head abs" style="left:45px">About Us</div>
  <ul class="footer-links abs">
    <li><svg width="12" height="12" viewBox="0 0 12 12"><circle cx="6" cy="6" r="5.2" fill="none" stroke="#fff"/><path d="M5 3.5 L7.5 6 L5 8.5" fill="none" stroke="#fff"/></svg>Home</li>
    <li><svg width="12" height="12" viewBox="0 0 12 12"><circle cx="6" cy="6" r="5.2" fill="none" stroke="#fff"/><path d="M5 3.5 L7.5 6 L5 8.5" fill="none" stroke="#fff"/></svg>Learn More</li>
    <li><svg width="12" height="12" viewBox="0 0 12 12"><circle cx="6" cy="6" r="5.2" fill="none" stroke="#fff"/><path d="M5 3.5 L7.5 6 L5 8.5" fill="none" stroke="#fff"/></svg>About Us</li>
    <li><svg width="12" height="12" viewBox="0 0 12 12"><circle cx="6" cy="6" r="5.2" fill="none" stroke="#fff"/><path d="M5 3.5 L7.5 6 L5 8.5" fill="none" stroke="#fff"/></svg>Schedule</li>
    <li><svg width="12" height="12" viewBox="0 0 12 12"><circle cx="6" cy="6" r="5.2" fill="none" stroke="#fff"/><path d="M5 3.5 L7.5 6 L5 8.5" fill="none" stroke="#fff"/></svg>Brinewardsea</li>
  </ul>

  <div class="footer-head abs" style="left:226px">Contact Us</div>
  <div class="ffield abs" style="left:230px;top:61px">Name</div>
  <div class="ffield abs" style="left:373px;top:61px">Phone</div>
  <div class="ffield abs" style="left:230px;top:100px">E-mail</div>
  <div class="ffield abs" style="left:373px;top:100px">Message</div>
  <div class="submit abs">SUBMIT</div>

  <div class="footer-head abs" style="left:583px;top:30px">Have Questions?</div>
  <div class="q-list abs">123-456-7890<br>Info@companyname.com<br>Lorem Ipsum is simply dummy</div>

  <div class="footer-head abs" style="left:844px">Follow Us</div>
  <span class="follow abs" style="left:840px" role="img" aria-label="Social network link"></span>
  <span class="follow abs" style="left:880px" role="img" aria-label="Social network link"></span>
  <span class="follow abs" style="left:921px" role="img" aria-label="Social network link"></span>
  <span class="follow abs" style="left:961px" role="img" aria-label="Social network link"></span>
</footer>

<div class="copyright abs">Copy Right @ 2016 Brinewardsea. All Rights Reserved</div>

</body>
</html>
```